Tolvar Mechanical Services Cultural Norms

Tale the uploaded list of cultural norms and develop a design that showcases how these 8 items encompass everything about our companies culture.

```html
<!DOCTYPE html>
<html lang="en">
<head>
<meta charset="utf-8">
<title>Tolvar Mechanical Services – Cultural Norms</title>
<link href="https://fonts.googleapis.com/css2?family=Montserrat:wght@500;700;800&family=Oswald:wght@700&display=swap" rel="stylesheet">
<style>
  :root{
    --navy:#2e3192;
    --rule:#f4455a;
    --heading:#0f6f8c;
    --body:#333a40;
    --ink:#2a2a2a;
    --white:#ffffff;
    --bg-top:#e8ecf1;
    --bg-bottom:#b7ccd4;
    --teal:#06708e;     --teal-d:#04536a;
    --cyan:#04a9c0;     --cyan-d:#03808f;
    --green:#03c17e;    --green-d:#02925f;
    --yellow:#fdb913;   --yellow-d:#c98a07;
    --orange:#f7901e;   --orange-d:#b8620c;
    --red:#f23f58;      --red-d:#b52b3e;
    --pink:#ff6a9d;     --pink-d:#c94878;
    --purple:#a068bf;   --purple-d:#6f4290;
  }
  *{box-sizing:border-box;margin:0;padding:0}
  html,body{width:1200px;height:900px;overflow:hidden}
  body{font-family:"Montserrat",sans-serif;background:var(--white)}
  .canvas{position:relative;width:1200px;height:900px;overflow:hidden;
    background:linear-gradient(180deg,var(--bg-top) 14%,var(--bg-bottom) 100%)}
  .masthead{position:absolute;left:0;top:0;width:1200px;height:117px;background:var(--white);
    border-bottom:7px solid var(--rule)}
  .brand{position:absolute;left:38px;top:24px;display:flex;align-items:center;gap:12px}
  .brand__mark{width:54px;height:54px;background:var(--ink)}
  .brand__name{font-weight:700;font-size:22px;line-height:26px;color:var(--ink);letter-spacing:.5px;text-transform:uppercase}
  .page-title{position:absolute;right:34px;top:10px;font-family:"Oswald",sans-serif;font-weight:700;
    font-size:84px;line-height:92px;color:var(--navy);letter-spacing:-.5px}

  .norm{position:absolute;width:525px;height:150px;--c:var(--teal);--d:var(--teal-d)}
  .norm svg{position:absolute;left:0;top:0;width:525px;height:150px}
  .norm__card{fill:var(--white);filter:drop-shadow(0 3px 5px rgba(0,0,0,.18))}
  .norm__tab{fill:var(--c)}
  .norm__fold{fill:var(--d)}
  .norm__cap{fill:var(--c)}
  .norm__cap-inner{fill:none;stroke:rgba(0,0,0,.08);stroke-width:2}
  .norm__num{position:absolute;left:0;top:38px;width:112px;text-align:center;color:var(--white);
    font-weight:800;font-size:64px;line-height:72px;letter-spacing:-1px}
  .norm__text{position:absolute;left:166px;top:26px;width:288px}
  .norm__title{font-weight:700;font-size:17px;line-height:22px;color:var(--heading);margin-bottom:9px;
    white-space:nowrap;letter-spacing:-.1px}
  .norm__desc{font-weight:500;font-size:12.3px;line-height:18.3px;color:var(--body)}
  .norm__text--three{top:20px}
  .norm__text--four{top:14px}

  .col-left{left:50px}
  .col-right{left:643px}
  .row-1{top:149px}.row-2{top:336px}.row-3{top:524px}.row-4{top:711px}

  .norm--teal{--c:var(--teal);--d:var(--teal-d)}
  .norm--cyan{--c:var(--cyan);--d:var(--cyan-d)}
  .norm--green{--c:var(--green);--d:var(--green-d)}
  .norm--yellow{--c:var(--yellow);--d:var(--yellow-d)}
  .norm--orange{--c:var(--orange);--d:var(--orange-d)}
  .norm--red{--c:var(--red);--d:var(--red-d)}
  .norm--pink{--c:var(--pink);--d:var(--pink-d)}
  .norm--purple{--c:var(--purple);--d:var(--purple-d)}
</style>
</head>
<body>
<main class="canvas">
  <header class="masthead">
    <div class="brand">
      <span class="brand__mark"></span>
      <span class="brand__name">Tolvar<br>Mechanical Services</span>
    </div>
    <h1 class="page-title">CULTURAL NORMS</h1>
  </header>

  <svg width="0" height="0" style="position:absolute">
    <defs>
      <symbol id="norm-shape" viewBox="0 0 525 150">
        <path class="norm__card" d="M100 8 H461 A61 61 0 0 1 461 130 H100 Z"/>
        <path class="norm__fold" d="M150 130 H176 L168 146 Z"/>
        <path class="norm__fold" d="M104 0 H114 L176 130 H164 Z"/>
        <path class="norm__tab" d="M40 0 H104 L164 148 H40 Q0 148 0 108 V40 Q0 0 40 0 Z"/>
        <path class="norm__cap" d="M461 18 A51 51 0 0 1 461 120 Z"/>
        <path class="norm__cap-inner" d="M461 44 A25 25 0 0 1 461 94"/>
      </symbol>
    </defs>
  </svg>

  <section class="norm norm--teal col-left row-1">
    <svg viewBox="0 0 525 150"><use href="#norm-shape"/></svg>
    <div class="norm__num">01</div>
    <div class="norm__text">
      <h2 class="norm__title">Continuous Improvement</h2>
      <p class="norm__desc">We believe that there is always room for improvement in everything we do</p>
    </div>
  </section>

  <section class="norm norm--cyan col-left row-2">
    <svg viewBox="0 0 525 150"><use href="#norm-shape"/></svg>
    <div class="norm__num">02</div>
    <div class="norm__text">
      <h2 class="norm__title">Enhancing Lives</h2>
      <p class="norm__desc">Our aimis to positively impact the lives of others through our actions and services.</p>
    </div>
  </section>

  <section class="norm norm--green col-left row-3">
    <svg viewBox="0 0 525 150"><use href="#norm-shape"/></svg>
    <div class="norm__num">03</div>
    <div class="norm__text norm__text--three">
      <h2 class="norm__title">Cultivating Encouragement</h2>
      <p class="norm__desc">We believe that fostering encouragement among our team members leads to personal fulfillment and opportunity.</p>
    </div>
  </section>

  <section class="norm norm--yellow col-left row-4">
    <svg viewBox="0 0 525 150"><use href="#norm-shape"/></svg>
    <div class="norm__num">04</div>
    <div class="norm__text norm__text--three">
      <h2 class="norm__title">Effective Communication</h2>
      <p class="norm__desc">We embracethe challenge of effective communication, recognizing its importance in our success.</p>
    </div>
  </section>

  <section class="norm norm--orange col-right row-1">
    <svg viewBox="0 0 525 150"><use href="#norm-shape"/></svg>
    <div class="norm__num">05</div>
    <div class="norm__text norm__text--three">
      <h2 class="norm__title">Think. Act. Take Ownership</h2>
      <p class="norm__desc">We operate by the mantra of thinking critically, executing, and taking ownership of our decisions.</p>
    </div>
  </section>

  <section class="norm norm--red col-right row-2">
    <svg viewBox="0 0 525 150"><use href="#norm-shape"/></svg>
    <div class="norm__num">06</div>
    <div class="norm__text norm__text--three">
      <h2 class="norm__title">Stay 1 Step Ahead</h2>
      <p class="norm__desc">We operate by the mantra of thinking critically, executing, and taking ownership of our decisions.</p>
    </div>
  </section>

  <section class="norm norm--pink col-right row-3">
    <svg viewBox="0 0 525 150"><use href="#norm-shape"/></svg>
    <div class="norm__num">07</div>
    <div class="norm__text norm__text--three">
      <h2 class="norm__title" style="font-size:16.6px;letter-spacing:-.3px">Creating Healthy Environments</h2>
      <p class="norm__desc">We are committed to establishing comfortable environments where our clients can thrive and be productive.</p>
    </div>
  </section>

  <section class="norm norm--purple col-right row-4">
    <svg viewBox="0 0 525 150"><use href="#norm-shape"/></svg>
    <div class="norm__num">08</div>
    <div class="norm__text norm__text--four">
      <h2 class="norm__title">Setting Higher Standards</h2>
      <p class="norm__desc">We aim to elevate the standards of the mechanical industry by educating both our customers and ourselves, constantly raising the bar.</p>
    </div>
  </section>
</main>
</body>
</html>
```